Packaging for Fog-Free Mirror & Astonishingly Superior Velko Shave Cream Promotion

Design package graphics for attached fog-free shower mirror product. Winner will also be given several other projects to design including other product packaging, presentations and web design (graphics only): SO THIS HAS A GOOD FUTURE FOR YOU!
I have attached a detailed description of what we hope to get from you including first attempt at design in PDF form so you can have a good running start! Included all logos, copy, layout, sizes, etc. EASY!
The look/feel of this package, like our other products, should be similar to the precision and clean lines of "Switzerland"/"Tarnel Ridge Tool Brand" or the German quality of "Holtz" or "Velda."
For our copy and positioning, we like the playful "Quibbets Mints" (curiously strong, astonishing, draw in your attention, quirky, etc.).
Updates
Added better PDF with new idea for you to think about :-) (foggy glass as background to show how great a FOG FREE mirror would be in the shower while you are shaving)
Hello and thanks for participating!
I have added a photo of a previous promotional pack that we offered (along lines of what you are doing here) with a full size shave cream (the one on this package is a sample 1/2 once size) and a similar 6" mirror (unframed in past, ours for this package will have a white frame). Please look at that to help shape new ideas.
Target Market(s)
men and women shopping who will buy this in a major US drug store chain
Industry/Entity Type
Product
Requirements
Must have
- Space on front for the "fog free" Mirror (the star of the package).
Space on back for the suction cup and the tube of the shave cream.
The copy as written somewhere on the front and back as indicated on the attached mock-up.
As for spacing, follow what we have here roughly.
Final design will be adjusted to fit the machine that will put this together in the card. I have included a sample photo of the type of package this will be like (SEE LUMEX sample next few pages).
I have also included the first version of our mocked-up package as a place for you to start and cut/paste art/logos.
BUT PLEASE BE CREATIVE AND MAKE IT LOOK ATTRACTIVE with GRAPHICS, COLOR, WHATEVER YOU SUGGEST!
Thanks!
Dave :-)

```html
<!DOCTYPE html>
<html lang="en">
<head>
<meta charset="utf-8">
<title>Velko Company Fog-Free Shower Mirror Card</title>
<link rel="stylesheet" href="https://fonts.googleapis.com/css2?family=Arimo:wght@400;700&display=swap">
<style>
  :root {
    --page: #ffffff;
    --navy: #1d2a4a;
    --brand-red: #c8102e;
    --white: #ffffff;
    --sky-deep: #1f5a9e;
    --sky-mid: #4d8fcf;
    --sky-light: #9fcdee;
    --sky-mist: #e4f2fb;
    --frame: #f3f0e2;
    --glass: #a9abad;
    --tube: #f1ede6;
    --tube-cap: #b3202a;
    --small-copy: #dbe8f4;
  }
  * { margin: 0; padding: 0; box-sizing: border-box; }
  html, body {
    width: 1200px; height: 900px; overflow: hidden;
    background: var(--page);
    font-family: "Arimo", Arial, sans-serif;
  }
  .card {
    position: absolute; left: 274px; top: 44px;
    width: 608px; height: 812px;
    border-radius: 16px; overflow: hidden;
    box-shadow: 4px 6px 10px rgba(0,0,0,0.35);
  }
  .card-backdrop {
    position: absolute; inset: 0;
    background:
      radial-gradient(ellipse 60% 30% at 20% 95%, var(--sky-mist) 0%, rgba(228,242,251,0) 70%),
      radial-gradient(ellipse 50% 30% at 90% 60%, rgba(159,205,238,0.7) 0%, rgba(159,205,238,0) 70%),
      linear-gradient(180deg, var(--sky-deep) 0%, var(--sky-mid) 45%, var(--sky-light) 85%, var(--sky-mist) 100%);
  }
  .hang-slot {
    position: absolute; left: 236px; top: 12px;
    width: 84px; height: 18px; border-radius: 9px;
    background: var(--page);
    box-shadow: inset 1px 2px 3px rgba(0,0,0,0.3);
  }
  .brand-name {
    position: absolute; left: 36px; top: 76px; width: 176px;
    text-align: center; white-space: nowrap;
    font-size: 15px; letter-spacing: 1.5px; color: var(--white);
  }
  .brand-rule {
    position: absolute; left: 10px; top: 96px; width: 232px; height: 2px;
    background: var(--white); opacity: 0.8;
  }
  .product-copy { position: absolute; left: 12px; top: 98px; color: var(--white); white-space: nowrap; }
  .product-copy .kicker { color: var(--brand-red); font-size: 17px; line-height: 19px; }
  .product-copy .title { font-size: 26px; line-height: 26px; }
  .product-copy .title-big { font-size: 34px; line-height: 34px; }
  .product-copy .sub { font-size: 17px; line-height: 18px; }
  .product-copy .spec {
    margin-top: 16px; font-size: 12px; line-height: 12px;
    letter-spacing: 0.4px; color: var(--small-copy);
  }
  .value-copy {
    position: absolute; right: 28px; top: 30px;
    text-align: center; color: var(--brand-red); white-space: nowrap;
    font-size: 24px; line-height: 26px;
  }
  .value-copy .headline { color: var(--white); font-size: 32px; line-height: 36px; }
  .mirror { position: absolute; left: 20px; top: 182px; width: 570px; height: 570px; }
  .mount-disc {
    position: absolute; left: 20px; top: 754px;
    width: 50px; height: 50px; border-radius: 50%;
    background: var(--white); border: 2px solid var(--frame);
  }
  .mount-copy, .sample-copy {
    position: absolute; color: var(--navy); font-size: 16px; line-height: 16px; white-space: nowrap;
  }
  .mount-copy { left: 76px; top: 758px; }
  .sample-copy { left: 412px; top: 752px; text-align: center; width: 150px; }
  .cream-tube {
    position: absolute; left: 566px; top: 716px;
    width: 28px; height: 74px; border-radius: 3px 3px 5px 5px;
    background: linear-gradient(180deg, var(--tube) 0%, var(--tube) 76%, var(--tube-cap) 76%, var(--tube-cap) 100%);
    box-shadow: 1px 2px 3px rgba(0,0,0,0.3);
  }
</style>
</head>
<body>
  <div class="card">
    <div class="card-backdrop" role="img" aria-label="Blue background photo of water droplets on fogged shower glass"></div>
    <div class="hang-slot"></div>

    <div class="brand-name">VELKO COMPANY</div>
    <div class="brand-rule"></div>

    <div class="product-copy">
      <p class="kicker">ASONISHING FOG FREE</p>
      <p class="title">shower mirror</p>
      <p class="title-big">fog-free</p>
      <p class="sub">break resistant</p>
      <p class="spec">6" diameter<br>premium<br>heavy-duty<br>polycarbonate</p>
    </div>

    <div class="value-copy">
      <p class="headline">SUPER VALUE!</p>
      <p>COMPARE TO</p>
      <p>SIMILAR FOGLESS</p>
      <p>MIRRORS FOR $12</p>
    </div>

    <svg class="mirror" viewBox="0 0 570 570" aria-label="Round fog-free mirror with white frame">
      <circle cx="285" cy="285" r="284" fill="var(--frame)"/>
      <circle cx="285" cy="285" r="271" fill="var(--glass)"/>
    </svg>

    <div class="mount-disc"></div>
    <p class="mount-copy">EASY MOUNT<br>suction cup included<br>(flip over)</p>

    <p class="sample-copy">FREE SAMPLE<br>shave cream<br>(flip over)</p>
    <div class="cream-tube" role="img" aria-label="Sample tube of Velko shave cream"></div>
  </div>
</body>
</html>
```